Now Leasing Banner

Looking for a banner that says the following information approx 4' x 30'

Now Leasing Maplewood Terrace 925-318-6054

Target Market(s)

Drive by traffic

Industry/Entity Type

Residential property management

Requirements
Must have
• Clear and readable from a distance

```html
<!DOCTYPE html>
<html lang="en">
<head>
<meta charset="UTF-8">
<title>Now Leasing Banner Options</title>
<link rel="stylesheet" href="https://fonts.googleapis.com/css2?family=Noto+Sans:wght@700&display=swap">
<style>
  :root {
    --canvas-bg: #000000;
    --panel-white: #fcfcfa;
    --navy: #033a57;
    --sage: #728b68;
    --apricot: #f0a35a;
    --ink-black: #000000;
    --text-light: #ffffff;
  }
  html, body {
    margin: 0;
    padding: 0;
    width: 1200px;
    height: 1200px;
    overflow: hidden;
    background: var(--canvas-bg);
  }
  .canvas {
    position: relative;
    width: 1200px;
    height: 1200px;
    font-family: "Noto Sans", "Segoe UI", sans-serif;
    font-weight: 700;
  }
  .banner {
    position: absolute;
    left: 4px;
    width: 1192px;
  }
  .banner--sage { top: 296px; }
  .banner--apricot { top: 520px; }
  .banner--navy { top: 743px; }

  .banner__headline {
    height: 80px;
    background: var(--panel-white);
    display: flex;
    align-items: center;
    justify-content: center;
    font-size: 49px;
    letter-spacing: -0.3px;
    color: var(--navy);
    margin: 0;
  }
  .banner--apricot .banner__headline { color: var(--ink-black); }

  .banner__contact {
    height: 80px;
    display: flex;
    align-items: center;
    justify-content: center;
    font-size: 37px;
    color: var(--text-light);
    margin: 0;
  }
  .banner--sage .banner__contact { background: var(--sage); }
  .banner--apricot .banner__contact { background: var(--apricot); }
  .banner--navy .banner__contact { background: var(--navy); }
</style>
</head>
<body>
  <main class="canvas">
    <section class="banner banner--sage">
      <h1 class="banner__headline">Now Leasing Maplewood</h1>
      <p class="banner__contact">Terrace 925-318-6054</p>
    </section>
    <section class="banner banner--apricot">
      <h1 class="banner__headline">Now Leasing Maplewood</h1>
      <p class="banner__contact">Terrace 925-318-6054</p>
    </section>
    <section class="banner banner--navy">
      <h1 class="banner__headline">Now Leasing Maplewood</h1>
      <p class="banner__contact">Terrace 925-318-6054</p>
    </section>
  </main>
</body>
</html>
```